New Web Page Design - Cement Rendering Business

Looking for a overhaul of our existing website (www.norpex.com.au).

Looking for a sleek and elegant design that incorporates the colours of our logos, black / green and white. Needs to look professional and want it to be well above what our competition is offering. (Findora search for 'cement rendering sydney' will display the competition we want to be well ahead of.

Prefer a mixture of pages with black background and white alternatively between home (black), about us (white), contact us (black) and gallery (white).

Would like to incorporate our logo on all pages attached preferably in the top left corner.

Website needs to be search engine optimised and have easily updated photo gallery which we already have.

Also need to embed our trackwise metrics code on the front home page.

Website needs to be able easily updated (text, pictures ) as required.
content management system should include fields where you can alter your page titles, meta description and keywords.

Pages also needs to be optimised for mobile devices, iphone, ipad and other mobile devices. (it is a current feature we have)

If you have any questions, just message me.

Please remember the look and feel of the site is important to us, we don't want it over complicated, simple elegant and professional in line with our logo standards.
Updates

Hi All, As an example of the look and feel we like. We have found a site that may assist in your design and creative process. http://demo.quorvix.org/ We like the simplicity, elegance and professional look of this site, although we would like it with our images, colours and logos. I hope this helps.! keep the great designs coming!

All, Thanks for the designs. Please try and use our website images due to copyright reasons for all your designs. Tomas

Target Market(s)

Construction Companies

Industry/Entity Type

Business

Colors
9bcb3b
acd036
474747

Requirements
Must have
• Search Engine Optimised.
Photo Gallery
Elegant/Professional Look & Feel.
Simple Yet Effective
Nice to have
• Moving Parts
Should not have
• Overly Complicated.
Cheap & Traditional Looking.
Boring

```html
<!DOCTYPE html>
<html lang="en">
<head>
<meta charset="utf-8">
<title>Norpex Rendering</title>
<link href="https://fonts.googleapis.com/css2?family=Open+Sans:ital,wght@0,300;0,400;0,600;0,700;1,300;1,400&display=swap" rel="stylesheet">
<style>
:root{
  --green:#9bcb3b;
  --green-2:#acd036;
  --charcoal:#474747;
  --black:#111111;
  --dark:#1c1c1c;
  --panel:#262626;
  --white:#ffffff;
  --paper:#f4f4f4;
  --text:#555555;
  --muted:#8a8a8a;
  --rule:#dddddd;
}
*{box-sizing:border-box;margin:0;padding:0}
html,body{width:726px;height:1200px;overflow:hidden}
body{font-family:"Open Sans",Arial,sans-serif;background:var(--white);color:var(--text);position:relative}
.wrap{width:500px;margin:0 auto;position:relative}

/* header */
.site-header{height:48px;background:var(--black)}
.site-header .wrap{height:48px;display:flex;align-items:center;width:620px}
.brand{display:flex;align-items:center;gap:9px}
.brand-dot{width:30px;height:30px;border-radius:50%;background:var(--green)}
.brand-name{color:var(--white);font-weight:700;font-size:21px;letter-spacing:1px}
.main-nav{margin-left:auto;display:flex;gap:28px;margin-right:28px}
.main-nav ul{list-style:none}
.main-nav li{font-size:5px;color:#aaa;line-height:7px;text-transform:uppercase;letter-spacing:.3px}
.main-nav li.active{color:var(--green)}
.social{display:flex;gap:4px;align-self:flex-start;margin-top:9px}
.social span{width:9px;height:9px;border-radius:50%;background:#d8d8d8;display:block}

/* hero */
.hero{height:278px;position:relative;background:linear-gradient(160deg,#3a3a3a 0%,#1e1e1e 35%,#5a5a5a 60%,#2a2a2a 100%)}
.hero-photo{position:absolute;inset:0;background:linear-gradient(90deg,rgba(0,0,0,.35),rgba(255,255,255,.06) 50%,rgba(0,0,0,.4))}
.hero-caption{position:absolute;left:0;right:0;top:142px;text-align:center}
.hero-caption .line-1{color:var(--white);font-size:11px;letter-spacing:1.4px;text-transform:uppercase}
.hero-caption .line-2{display:inline-block;margin-top:4px;padding:3px 30px;background:rgba(155,203,59,.85);color:var(--white);font-size:11px;letter-spacing:1.4px;text-transform:uppercase}

.slider-dots{display:flex;justify-content:center;gap:5px;margin-top:20px}
.slider-dots span{width:5px;height:5px;border-radius:50%;background:#333}
.slider-dots span.on{background:var(--green)}

/* tagline */
.tagline{text-align:center;font-style:italic;font-weight:300;font-size:22px;line-height:27px;color:#444;margin-top:22px}
.tagline-rule{height:2px;background:#222;margin-top:24px}

/* section heads */
.section-head{display:flex;justify-content:space-between;align-items:flex-end;border-bottom:1px solid var(--rule);padding-bottom:4px}
.section-head h2{font-size:7px;font-weight:700;color:#222;text-transform:uppercase;letter-spacing:.4px;position:relative}
.section-head h2::after{content:"";position:absolute;left:0;bottom:-5px;width:30px;height:2px;background:#222}
.section-head a{font-size:5px;color:var(--muted);text-decoration:none}

/* featured */
.featured{margin-top:32px}
.work-grid{display:grid;grid-template-columns:repeat(3,1fr);gap:8px;margin-top:12px}
.work{height:88px}
.work.w1{background:linear-gradient(135deg,#9a9a93,#c9c6bd 55%,#d07a2f)}
.work.w2{background:linear-gradient(135deg,#6f6e6a,#9c9b96 50%,#b5b2ac)}
.work.project{background:var(--green);display:flex;flex-direction:column;align-items:center;justify-content:center;color:var(--white)}
.work.project strong{font-size:9px;font-weight:600}
.work.project small{font-size:5px;opacity:.9;margin-top:2px}
.work.w4{background:linear-gradient(135deg,#d9d9d9,#a8a8a8 60%,#7d7d7d)}
.work.w5{background:linear-gradient(135deg,#8c7b64,#b69d7a 50%,#6d6253)}
.work.w6{background:linear-gradient(135deg,#9ab6cf,#c7b89a 55%,#7a6c55)}

/* about */
.about{margin-top:16px}
.about-body{display:flex;gap:30px;margin-top:14px}
.about-left{width:230px}
.about-icons{display:flex;gap:8px}
.about-icons span{width:30px;height:30px;border-radius:50%;background:#222;display:flex;align-items:center;justify-content:center}
.about-icons span.on{background:var(--green);width:36px;height:36px;margin-top:-3px}
.about-icons svg{width:14px;height:14px}
.small-copy{font-size:5px;line-height:7px;color:var(--muted);margin-top:10px}
.btn{display:inline-block;background:#1a1a1a;color:var(--white);font-size:5px;padding:3px 8px;margin-top:8px}
.about-right{flex:1;padding-top:18px}
.about-right h3{display:flex;align-items:center;gap:7px;font-size:11px;font-weight:600;color:#333}
.about-right h3::before{content:"";width:12px;height:12px;border-radius:50%;background:var(--green)}
.about-right .sub{font-size:8px;color:#555;margin-top:5px}

/* services */
.services{margin-top:22px}
.service-grid{display:grid;grid-template-columns:repeat(3,1fr);gap:10px;margin-top:14px}
.service-title{height:16px;background:#1e1e1e;display:flex;align-items:center;gap:5px;padding-left:8px;font-size:5px;font-weight:700;color:var(--white);text-transform:uppercase}
.service-title::before{content:"";width:6px;height:6px;border-radius:50%;background:var(--green)}
.service-body{height:64px;background:var(--panel);margin-top:3px;padding:7px 8px;font-size:5px;line-height:7px;color:#b0b0b0}
.service.mid .service-body{background:var(--green);color:#1e1e1e}
.service .btn{margin-top:5px}

/* footer */
.site-footer{position:absolute;left:0;right:0;bottom:0;height:124px;background:var(--dark)}
.footer-cols{display:flex;gap:20px;padding-top:10px}
.footer-col{flex:1}
.footer-col h4{font-size:11px;font-weight:400;color:#ddd}
.footer-col p,.footer-col li{font-size:5px;line-height:7px;color:#888;list-style:none}
.footer-col .block{margin-top:6px}
.news-form{display:flex;margin-top:8px}
.news-form span{flex:1;height:10px;background:var(--white)}
.news-form b{width:22px;height:10px;background:var(--charcoal)}
.footer-social{display:flex;gap:6px;margin-top:8px;justify-content:flex-end}
.footer-social span{width:7px;height:7px;background:#666;display:block}
.copyright{font-size:5px;color:#777;margin-top:4px}
</style>
</head>
<body>

<header class="site-header">
  <div class="wrap">
    <div class="brand"><span class="brand-dot"></span><span class="brand-name">NORPEX</span></div>
    <nav class="main-nav">
      <ul><li class="active">Home</li><li>Services</li><li>Projects</li><li>About</li></ul>
      <ul><li>Testimonials</li><li>News</li><li>Gallery</li><li>Careers</li><li>Contact</li></ul>
    </nav>
    <div class="social"><span></span><span></span><span></span><span></span></div>
  </div>
</header>

<section class="hero">
  <div class="hero-photo" role="img" aria-label="Black and white photo looking up at a rendered high-rise facade with rows of windows"></div>
  <div class="hero-caption">
    <div class="line-1">This is the architecture and interior showcase</div>
    <div class="line-2">We have new fresh ideas all the time</div>
  </div>
</section>

<div class="slider-dots"><span></span><span class="on"></span><span></span></div>

<div class="wrap">
  <p class="tagline">We have 10 years of experience in this feild.<br>We know what you want.</p>
  <div class="tagline-rule"></div>

  <section class="featured">
    <div class="section-head"><h2>Featured Works</h2><a>View All Works</a></div>
    <div class="work-grid">
      <div class="work w1" role="img" aria-label="Photo of a trowel and render tools on a wall"></div>
      <div class="work w2" role="img" aria-label="Photo of a worker rendering a wall"></div>
      <div class="work project"><strong>Project Title Here</strong><small>Cement rendering, Sydney</small></div>
      <div class="work w4" role="img" aria-label="Photo of a freshly rendered white wall"></div>
      <div class="work w5" role="img" aria-label="Photo of a plasterer applying render"></div>
      <div class="work w6" role="img" aria-label="Photo of a rendered house exterior"></div>
    </div>
  </section>

  <section class="about">
    <div class="section-head"><h2>About Us</h2></div>
    <div class="about-body">
      <div class="about-left">
        <div class="about-icons">
          <span><svg viewBox="0 0 14 14"><rect x="3" y="4" width="8" height="6" fill="#fff"/></svg></span>
          <span><svg viewBox="0 0 14 14"><rect x="2" y="5" width="7" height="4" fill="#fff"/><circle cx="11" cy="10" r="2" fill="#fff"/></svg></span>
          <span><svg viewBox="0 0 14 14"><circle cx="7" cy="7" r="4" fill="none" stroke="#fff" stroke-width="1.5"/></svg></span>
          <span class="on"><svg viewBox="0 0 14 14"><path d="M3 7l3 3 5-6" fill="none" stroke="#fff" stroke-width="1.8"/></svg></span>
        </div>
        <p class="small-copy">We are a Sydney based cement rendering team with over ten years of experience in our field. Our crews finish homes, offices and commercial builds with care, on time and to the highest standard of quality.</p>
        <span class="btn">Read More</span>
      </div>
      <div class="about-right">
        <h3>Amet Ornare Magna Porta</h3>
        <p class="sub">Fusce dapibus, tellus ac cursus commodo</p>
        <p class="small-copy">Solid render coats applied by skilled trades who take pride in clean lines and lasting finishes. We work closely with builders and owners from the first quote through to final handover, keeping every site tidy and safe. Our acrylic and cement systems suit new builds and renovations alike, and each job is checked by a supervisor before we sign off on the work.</p>
      </div>
    </div>
  </section>

  <section class="services">
    <div class="section-head"><h2>Our Service</h2></div>
    <div class="service-grid">
      <div class="service">
        <div class="service-title">How We Work</div>
        <div class="service-body">We visit the site, measure and quote the job, then plan each stage with the builder so render is applied at the right time and every wall cures evenly.</div>
        <span class="btn">Read More</span>
      </div>
      <div class="service mid">
        <div class="service-title">Philosophy</div>
        <div class="service-body">Quality first, every time. We believe a smooth, lasting finish comes from honest work, good materials and a crew that cares about the result.</div>
      </div>
      <div class="service">
        <div class="service-title">Why You Choose Us</div>
        <div class="service-body">Fully licensed and insured, ten years of proven projects, fair pricing and a team that turns up when promised and leaves the site clean.</div>
        <span class="btn">Read More</span>
      </div>
    </div>
  </section>
</div>

<footer class="site-footer">
  <div class="wrap">
    <div class="footer-cols">
      <div class="footer-col">
        <h4>Contact detail</h4>
        <p class="block">Unit 4, 18 Harbour Lane<br>Redfield NSW 2000</p>
        <p class="block">Phone: (02) 5550 1842<br>Mobile: 0400 555 219<br>info@norpex.com.au</p>
      </div>
      <div class="footer-col">
        <h4>Useful links</h4>
        <ul class="block"><li>Home Page</li><li>About Our Team</li><li>Services</li><li>Project Gallery</li><li>Testimonials</li><li>Contact Us</li></ul>
      </div>
      <div class="footer-col">
        <h4>Don't miss out</h4>
        <p class="block">Sign up for our newsletter to hear about new projects and offers.</p>
        <div class="news-form"><span></span><b></b></div>
        <div class="footer-social"><span></span><span></span><span></span><span></span><span></span></div>
      </div>
    </div>
    <p class="copyright">Copyright 2024 Norpex Rendering. All rights reserved.</p>
  </div>
</footer>

</body>
</html>
```